Tidewell Recovery Business Card Design

Professional and clean design. The design colors should flow with the logo. Two-sided card with the website on the back which is:

www.TidewellRecovery.example.

"Specializing in Water Damage Restoration"

On the front I need the name, email, phone, and logo.

Name: Dorian Vashti
Email: Dorian@TidewellRecovery.example
Phone: 555-318-2046 for now

I only have the Preview and Thumbnail right now but should have the source files uploaded within a day or two.

Target Market(s)

Flood victims, home owners with water damage from busted pipes etc...

Industry/Entity Type

Business

Contact Information for Business Card

Name: Dorian Vashti

Font styles to use
Serif
Sans Serif

```html
<!DOCTYPE html>
<html lang="en">
<head>
<meta charset="utf-8">
<title>Tidewell Recovery Business Card</title>
<link rel="stylesheet" href="https://fonts.googleapis.com/css2?family=Cinzel:wght@400;600&family=Source+Sans+3:wght@400&display=swap">
<style>
  :root {
    --page-bg: #ececec;
    --card-white: #ffffff;
    --brand-blue: #2b98d6;
    --light-blue: #5ec2f0;
    --deep-blue: #2a90d2;
    --text-blue: #3399d4;
    --text-dark: #262626;
    --text-grey: #4a4a4a;
    --divider: #c9c9c9;
  }
  * { margin: 0; padding: 0; box-sizing: border-box; }
  html, body {
    width: 1200px;
    height: 1188px;
    overflow: hidden;
    background: var(--page-bg);
  }
  .canvas { position: relative; width: 1200px; height: 1188px; }

  .card {
    position: absolute;
    width: 910px;
    height: 521px;
    border-radius: 36px;
    overflow: hidden;
    box-shadow: 0 4px 14px rgba(0,0,0,0.18);
  }
  .card-front { left: 68px; top: 52px; background: var(--card-white); }
  .card-back { left: 240px; top: 627px; background: var(--brand-blue); }

  .front-waves { position: absolute; left: 0; top: 0; width: 910px; height: 521px; }

  .brand-block {
    position: absolute;
    left: 40px;
    top: 92px;
    width: 384px;
    text-align: center;
  }
  .brand-dot {
    display: block;
    width: 104px;
    height: 104px;
    margin: 0 auto 18px;
    border-radius: 50%;
    background: var(--text-blue);
  }
  .brand-name {
    font-family: 'Cinzel', serif;
    font-weight: 600;
    font-size: 38px;
    line-height: 42px;
    color: var(--text-blue);
    letter-spacing: 1px;
  }

  .divider {
    position: absolute;
    left: 442px;
    top: 97px;
    width: 2px;
    height: 203px;
    background: var(--divider);
  }

  .person {
    position: absolute;
    left: 468px;
    top: 100px;
  }
  .person-name {
    font-family: 'Cinzel', serif;
    font-weight: 400;
    font-size: 34px;
    color: var(--text-blue);
    letter-spacing: 1px;
    line-height: 40px;
  }
  .person-title {
    font-family: 'Cinzel', serif;
    font-size: 28px;
    color: var(--text-grey);
    letter-spacing: 3px;
    line-height: 36px;
  }

  .contact-list {
    position: absolute;
    left: 468px;
    top: 198px;
    list-style: none;
    font-family: 'Source Sans 3', sans-serif;
    font-size: 22px;
    color: var(--text-dark);
  }
  .contact-list li {
    display: flex;
    align-items: center;
    height: 36px;
  }
  .contact-icon { width: 18px; height: 18px; margin-right: 12px; flex: none; }

  .address {
    position: absolute;
    right: 48px;
    top: 448px;
    text-align: right;
    font-family: 'Source Sans 3', sans-serif;
    font-style: normal;
    font-size: 21px;
    line-height: 25px;
    color: var(--text-dark);
  }

  .back-brand {
    position: absolute;
    left: 0;
    top: 90px;
    width: 100%;
    text-align: center;
  }
  .back-dot {
    display: block;
    width: 150px;
    height: 150px;
    margin: 0 auto 24px;
    border-radius: 50%;
    background: var(--card-white);
  }
  .back-name {
    font-family: 'Cinzel', serif;
    font-weight: 600;
    font-size: 40px;
    line-height: 48px;
    color: var(--card-white);
    letter-spacing: 1px;
  }
  .tagline {
    position: absolute;
    left: 0;
    top: 392px;
    width: 100%;
    text-align: center;
    font-family: 'Cinzel', serif;
    font-size: 26px;
    line-height: 32px;
    color: var(--card-white);
    letter-spacing: 1.5px;
  }
  .back-website {
    position: absolute;
    left: 0;
    top: 440px;
    width: 100%;
    text-align: center;
    font-family: 'Source Sans 3', sans-serif;
    font-size: 22px;
    line-height: 28px;
    color: var(--card-white);
    letter-spacing: 0.5px;
  }
</style>
</head>
<body>
<main class="canvas">

  <section class="card card-front" aria-label="Card front">
    <svg class="front-waves" viewBox="0 0 910 521" aria-hidden="true">
      <path fill="var(--light-blue)" d="M0 345 C 60 400, 150 460, 230 475 C 420 505, 650 420, 910 395 L 910 521 L 0 521 Z"/>
      <path fill="var(--deep-blue)" d="M0 322 C 70 380, 150 440, 230 475 C 150 445, 70 400, 0 360 Z"/>
      <path fill="var(--deep-blue)" d="M630 420 C 720 385, 820 360, 910 352 L 910 372 C 820 378, 720 395, 630 420 Z"/>
    </svg>

    <div class="brand-block">
      <span class="brand-dot"></span>
      <div class="brand-name">Tidewell<br>Recovery</div>
    </div>

    <div class="divider"></div>

    <div class="person">
      <div class="person-name">Dorian Vashti</div>
      <div class="person-title">Title</div>
    </div>

    <ul class="contact-list">
      <li>
        <svg class="contact-icon" viewBox="0 0 18 18" aria-hidden="true">
          <circle cx="9" cy="9" r="8" fill="none" stroke="var(--text-blue)" stroke-width="1.6"/>
          <path d="M6 5 L8 5 L8.6 7.5 L7.5 8.3 Q8.5 10.5 10 11 L10.8 10 L13 10.6 L13 12.4 Q8 13 5.5 7 Z" fill="var(--text-blue)"/>
        </svg>
        <span>555-318-2046</span>
      </li>
      <li>
        <svg class="contact-icon" viewBox="0 0 18 18" aria-hidden="true">
          <rect x="1.5" y="4" width="15" height="11" rx="1.5" fill="var(--text-blue)"/>
          <path d="M2 5 L9 10.5 L16 5" fill="none" stroke="#fff" stroke-width="1.4"/>
        </svg>
        <span>Dorian@TidewellRecovery.example</span>
      </li>
      <li>
        <svg class="contact-icon" viewBox="0 0 18 18" aria-hidden="true">
          <g fill="none" stroke="var(--text-blue)" stroke-width="1.3">
            <circle cx="9" cy="9" r="7.5"/>
            <ellipse cx="9" cy="9" rx="3.2" ry="7.5"/>
            <path d="M1.5 9 H16.5 M3 5 H15 M3 13 H15"/>
          </g>
        </svg>
        <span>www.TidewellRecovery.example</span>
      </li>
    </ul>

    <address class="address">
      Street Name, City Name<br>
      Zipcode-12345
    </address>
  </section>

  <section class="card card-back" aria-label="Card back">
    <div class="back-brand">
      <span class="back-dot"></span>
      <div class="back-name">Tidewell Recovery</div>
    </div>
    <p class="tagline">Specializing in Water Damage Restoration</p>
    <p class="back-website">www.TidewellRecovery.example</p>
  </section>

</main>
</body>
</html>
```